C U B A N - C I G A R S - F L Y E R

I need a double-sided 5x7 club type flyer for a Memorial Day Weekend Trip.
The main side design needs to be similar to the attached flyer example. The front design of flyer is KEY. The design will be awarded to the closest finished submission to the example flyer.
Both sides of the flyer should also included event and business logo, which are also attached. Both logos can be altered to fit printing need accordingly.
Front side content is also attached.
The back side design will be very simple. Consists of 3 travel images and trip description, and my contact very details. Same color design as front. The attached word document contains backside details for REFERENCE ONLY. Please focus on front side when submitting a design for this project.
Target Market(s)
A F R I C A N - A M E R I C A N - C I G A R - S M O K E R S
Industry/Entity Type
Travel Industry
Requirements
Must have
- All the elements of the attached information
Nice to have
- Masculine Images
Should not have
- Large Cigar focus to catch customer's attention

```html
<!DOCTYPE html>
<html lang="en">
<head>
<meta charset="utf-8">
<title>Cuba Cigar Gentlemen's Memorial Day Weekend Flyer</title>
<link rel="stylesheet" href="https://fonts.googleapis.com/css2?family=Archivo+Black&family=Open+Sans:wght@400;600;700;800&display=swap">
<style>
:root{
  --bg:#c7d0da;
  --blue-light:#8fb0de;
  --blue-mid:#6d93cf;
  --blue-dark:#1f3c8e;
  --pink:#f08a92;
  --maroon:#7a1420;
  --white:#ffffff;
  --ink:#1a1a1a;
  --photo-dark:#2a2a2e;
  --photo-mid:#5c5a5e;
}
*{margin:0;padding:0;box-sizing:border-box}
html,body{width:1200px;height:857px;overflow:hidden;background:var(--bg);font-family:"Open Sans",Arial,sans-serif}
.sheet{position:absolute;top:50px;width:540px;height:756px;overflow:hidden;background:var(--white);box-shadow:0 4px 14px rgba(0,0,0,.18)}
.front{left:30px}
.back{left:630px}

/* FRONT */
.front .column{position:absolute;left:0;top:0;width:250px;height:100%;background:var(--blue-light)}
.front .rule{position:absolute;top:0;width:6px;height:100%;background:var(--blue-dark)}
.front .rule.left{left:14px}
.front .rule.right{left:238px}
.front .photo{position:absolute;left:244px;top:0;width:296px;height:100%;background:linear-gradient(160deg,var(--photo-mid) 0%,var(--photo-dark) 55%,#151517 100%)}
.logo-box{position:absolute;left:28px;top:28px;width:204px;height:190px;background:var(--white);display:flex;align-items:center;justify-content:center}
.event-mark{width:160px;height:160px;border:4px solid var(--blue-dark);border-radius:50%;display:flex;align-items:center;justify-content:center;text-align:center;font-family:"Archivo Black",sans-serif;font-size:21px;line-height:1.1;color:var(--blue-dark)}
.title{position:absolute;left:28px;top:236px;width:330px}
.title .main{font-family:"Archivo Black",sans-serif;font-size:66px;line-height:.92;color:var(--blue-dark);letter-spacing:1px}
.title .sub{margin-top:8px;font-family:"Archivo Black",sans-serif;font-size:23px;line-height:1.05;color:var(--white)}
.tag-bar{position:absolute;left:20px;top:452px;width:330px;height:70px;background:var(--blue-dark);padding:8px 14px;font-family:"Archivo Black",sans-serif;font-size:23px;line-height:1.1;color:var(--white)}
.details{position:absolute;left:20px;top:522px;width:360px;height:234px;background:var(--pink);padding:10px 14px;color:var(--ink);font-size:11.5px;line-height:1.2}
.details .lead{font-weight:600}
.details .accent{color:var(--blue-dark);font-weight:800}
.details .big{font-family:"Archivo Black",sans-serif;font-size:19px;line-height:1;color:var(--blue-dark);margin:3px 0}
.details .label{color:var(--blue-dark);font-weight:800;margin-top:3px}
.details .phone{font-family:"Archivo Black",sans-serif;font-size:17px;color:var(--blue-dark);line-height:1.1}
.starburst{position:absolute;left:388px;top:515px;width:130px;height:130px}
.biz-mark{position:absolute;left:420px;top:648px;width:100px;height:100px;border:3px solid var(--white);border-radius:50%;display:flex;align-items:center;justify-content:center;text-align:center;font-size:12px;font-weight:700;line-height:1.2;color:var(--white)}

/* BACK */
.back .gallery{position:absolute;left:14px;top:14px;right:14px;height:92px;display:flex;gap:10px}
.back .gallery .shot{flex:1;border:4px solid var(--blue-dark);border-radius:14px}
.shot.car{background:linear-gradient(135deg,#b07a6a,#5a5050)}
.shot.map{background:linear-gradient(135deg,#bcd8f2,#e9eef4)}
.shot.cigars{background:linear-gradient(135deg,#7a4a2a,#c08a4a)}
.back .story{position:absolute;left:0;top:112px;width:100%;height:200px;background:var(--pink);padding:10px 16px;color:var(--maroon);font-size:9.6px;line-height:1.3;text-align:justify}
.back .scene{position:absolute;left:0;top:312px;width:100%;height:380px;background:linear-gradient(180deg,#e6e6e8,#f3f3f4 70%,#ffffff)}
.panel{position:absolute;background:var(--blue-mid);border:5px solid var(--blue-dark);color:var(--white);border-top:none}
.panel.price{left:40px;top:340px;width:230px;height:240px;border-radius:0 0 60px 60px;padding:18px 18px;font-size:14.5px;line-height:1.3}
.panel.included{left:290px;top:312px;width:225px;height:252px;border-radius:0 0 60px 60px;padding:14px 16px;font-size:11.5px;line-height:1.3}
.panel .strong{font-weight:800;color:var(--blue-dark)}
.panel .heading{font-size:15px;font-weight:600;margin-bottom:3px}
.back .terms{position:absolute;left:130px;top:592px;width:290px;font-size:14px;line-height:1.3;color:var(--ink);text-align:right}
.back .terms .strong{font-weight:800;color:var(--blue-dark)}
.event-mark.small{position:absolute;left:30px;top:600px;width:86px;height:86px;border-width:3px;font-size:12px}
.biz-mark.small{left:440px;top:592px;width:70px;height:70px;border-color:var(--blue-dark);color:var(--blue-dark);font-size:9px}
.back .call{position:absolute;left:0;bottom:0;width:100%;height:64px;background:var(--pink);display:flex;align-items:center;justify-content:center;font-size:18px;font-weight:800;color:var(--ink)}
</style>
</head>
<body>

<section class="sheet front">
  <div class="column"></div>
  <div class="photo" role="img" aria-label="Photo of a man in sunglasses and a dark jacket lighting a cigar"></div>
  <div class="rule left"></div>
  <div class="rule right"></div>

  <div class="logo-box"><div class="event-mark">Malecón<br>Weekend</div></div>

  <div class="title">
    <div class="main">CUBA<br>CIGAR</div>
    <div class="sub">GENTLEMEN'S<br>MEMORIAL DAY<br>WEEKEND</div>
  </div>

  <div class="tag-bar">CIGARS, RUM, &amp;<br>CLASSIC CARS..</div>

  <div class="details">
    <div class="lead">Legally travel to Cuba and return<br>with real <span class="accent">CUBAN CIGARS!</span></div>
    <div class="label">Trip Name:</div>
    <div>Rum Cigars and Classic Cars</div>
    <div class="big">MEMORIAL DAY<br>WEEKEND 2018!</div>
    <div class="label">Dates:</div>
    <div>Friday, May 25th<br>Tuesday May 29th</div>
    <div class="label">For More Information Call:</div>
    <div class="phone">XXX-XXX-XXXX</div>
    <div class="label">Book Today at</div>
    <div>www.cigarjourneys.example/CUBA2018</div>
  </div>

  <svg class="starburst" viewBox="0 0 130 130">
    <polygon fill="#ffffff" points="65,2 73,22 90,8 91,30 112,22 104,43 127,45 110,60 128,74 106,80 116,101 94,99 95,122 76,110 65,128 54,110 35,122 36,99 14,101 24,80 2,74 20,60 3,45 26,43 18,22 39,30 40,8 57,22"/>
    <text x="65" y="56" text-anchor="middle" font-family="Archivo Black, sans-serif" font-size="19" fill="#1f3c8e">BOOK</text>
    <text x="65" y="76" text-anchor="middle" font-family="Archivo Black, sans-serif" font-size="19" fill="#1f3c8e">NOW!</text>
    <text x="65" y="92" text-anchor="middle" font-family="Open Sans, sans-serif" font-size="10" font-weight="700" fill="#1a1a1a">SPACE IS LIMITED</text>
  </svg>

  <div class="biz-mark">Harbor Route<br>Travel</div>
</section>

<section class="sheet back">
  <div class="gallery">
    <div class="shot car" role="img" aria-label="Classic pink American car"></div>
    <div class="shot map" role="img" aria-label="Map of Cuba"></div>
    <div class="shot cigars" role="img" aria-label="Close-up of Cuban cigars"></div>
  </div>

  <p class="story">Cuba is the ultimate bucket list destination for any cigar lover. Now is your opportunity to legally travel to Cuba and experience a country that has been off limits to Americans for more than 50 years before it changes. Smoke fine Cuban cigars, meet its resilient people and experience Cuba's fascinating culture. Tour cigar factories, watch expert cigar rollers, visit a humidor factory and work shop, tour the Old Harbor Rum Museum to learn firsthand the process of making rum followed by rum tasting and pairings with Cuban cigars in a private setting and much more. Explore the Pinar Del Rio located in the Viñales Valley known for its stunning land scapes and tobacco plantations. Visit the world famous Vega Verde Tobacco Plantation to see first hand where and how the tobacco process is grown for fine Cuban cigars. The bucket list trip of a lifetime awaits on this 'people to people' Cigar Journey to Cuba to learn first hand about Cuban cigars, meet the Cuban people, experience incredible cuisine, drive in classic American cars along the Malecon and experience the Cuban cigar process from 'seed to smoke' and an opportunity to smoke in the birthplace of cigars!</p>

  <div class="scene" role="img" aria-label="Faded photo of a man lighting a cigar"></div>

  <div class="panel price">
    <div><span class="strong">Trip Cost:</span> $2050</div>
    <div><span class="strong">Deposit:</span> $300</div>
    <div>Payment plans available</div>
    <div><span class="strong">$300</span> Deposit Required</div>
    <div>Final payment Due By<br>April 10, 2018</div>
    <div>*NON-REFUNDABLE<br>*Passport Required</div>
  </div>

  <div class="panel included">
    <div class="heading">What's Included:</div>
    <div>4 Days / 3 Nights</div>
    <div>5 Star Hotel Accommodations Based on Double Occupancy</div>
    <div>Roundtrip Coastal Wings Airline Tickets from Fort Lauderdale Florida - Cuba</div>
    <div>Tour Bus Chauffeured Transportation</div>
    <div>All Rum and Cigar Tour Events</div>
    <div>Select Meals (Breakfast, Welcome and Farewell Dinner) and More!</div>
  </div>

  <div class="biz-mark small">Harbor Route<br>Travel</div>

  <div class="terms">
    <div><span class="strong">$300</span> Deposit Required</div>
    <div>Final payment Due By April 10, 2018</div>
    <div>*NON-REFUNDABLE</div>
    <div>*Passport Required</div>
  </div>

  <div class="event-mark small">Malecón<br>Weekend</div>

  <div class="call">For More Information Call:&nbsp;<span>XXX-XXX-XXXX</span></div>
</section>

</body>
</html>
```